Consulting & Education Company Needs Dynamic MS Word Template

We need a MS Word Template for everyday documents. This would be leveraged to create reports, marketing materials, internal memos etc.

The document should follow the standard MS Word template format and have an H1,H2,H3, paragraph, Title, bold font, regular font, table etc. All editable with normal MS Word features.

Attached is a Logo which was created by one of the many talented folks here at ArtHarbor. We would like to see the same color scheme used throughout the document. Additional attached is a sample word document that outlines all of the components we would like to see in the template.

Target Market(s)

Information Security - Penetration Testing - IT - Network/Systems Engineering

Industry/Entity Type

Education

Requirements
Must have
• Submission must meet all standard MS Word Template requirements.
• Submission should make use of Built in MS Styles so as the user of the template I shoudl be able to create a brand new page and insert an H1 for example and be able to select from the styles drop down the same font/color/style that you have designed for your submission.
• All sections in the provided document need to be contained in your submission.
• The table of contents should auto update if I add a new page, heading, section etc.
• Need to read and understand all of my comments which I have placed in the sample document uploaded to the briefing
Nice to have
• the cover page should be eye catching but not over the top. Some cool vectors/bg colors etc that look nice with the logo already provided.
• Icons and vectors whever they make sense and are visually appealing. For example the document has a section for defiing severity risk: Critical, High, Medium and Low it would be great if there was a nice icon or 2d graphic associated with each one. also color coded is a plus High is more dangerous then medium so the colors should communicate that.
Should not have
• no fixed textboxes or image boxes. everything needs to be smoothly editable in MS Word. "Editable" means more than just being able to alter text.

```html
<!DOCTYPE html>
<html lang="en">
<head>
<meta charset="utf-8">
<title>Probewise – Report Template Pages</title>
<link href="https://fonts.googleapis.com/css2?family=Montserrat:wght@500;600;700&family=Open+Sans:wght@400;600;700&display=swap" rel="stylesheet">
<style>
  :root{
    --red:#d71920;
    --ink:#2b2b2b;
    --slate:#3a4149;
    --slate-2:#4b5058;
    --grey:#a7a9ac;
    --sheet:#ececec;
    --low:#1ba1c9;
    --med:#f26b0f;
    --high:#d71920;
    --crit:#4a3f35;
    --head:'Montserrat',sans-serif;
    --body:'Open Sans',sans-serif;
  }
  *{box-sizing:border-box;margin:0;padding:0}
  html,body{width:1200px;height:1200px;overflow:hidden;background:#fff}
  body{position:relative;font-family:var(--body);color:var(--ink)}

  .sheet-row{position:absolute;left:20px;width:1160px;height:376px;background:var(--sheet);display:flex;gap:6px;padding:6px 10px}
  .row-1{top:12px}.row-2{top:412px}.row-3{top:812px}

  .page{position:relative;width:280px;height:362px;background:#fff;border:1px solid #dcdcdc;overflow:hidden}

  .brand{position:absolute;top:14px;right:14px;display:flex;align-items:center;gap:3px;font-family:var(--head);font-weight:700;font-size:6.5px;color:var(--red);letter-spacing:.2px}
  .brand i{display:block;width:7px;height:7px;background:var(--red)}

  .page-foot{position:absolute;left:4px;right:4px;top:342px;height:16px}
  .page-foot .band{position:absolute;left:0;top:0;bottom:0;right:20px;background:var(--red);clip-path:polygon(0 0,calc(100% - 8px) 0,100% 100%,0 100%);color:#fff;font-size:4.3px;display:flex;align-items:center;padding-left:10px;gap:6px}
  .page-foot .num{position:absolute;right:10px;font-size:4.5px}
  .page-foot .tab{position:absolute;right:0;top:0;bottom:0;width:30px;background:var(--slate);clip-path:polygon(0 0,100% 0,100% 100%,35% 100%)}

  .content{position:absolute;left:32px;right:32px;top:44px}
  h2{font-family:var(--head);font-weight:600;font-size:11.5px;color:var(--ink);margin:0 0 4px;letter-spacing:.1px}
  h2.red{color:var(--red)}
  h3{font-family:var(--head);font-weight:600;font-size:11px;color:var(--ink);margin:0 0 4px}
  p.txt{font-size:4.4px;line-height:1.4;text-align:justify;color:#333}
  .gap{height:10px}

  /* cover */
  .cover .brand{top:30px;left:24px;right:auto;font-size:15px;gap:5px}
  .cover .brand i{width:17px;height:17px}
  .cover-title{position:absolute;left:4px;top:88px;width:222px;height:64px;background:var(--red);clip-path:polygon(0 0,100% 0,80% 100%,0 100%);color:#fff;padding:15px 0 0 30px;font-family:var(--head)}
  .cover-title .client{font-size:9.5px;font-weight:500}
  .cover-title .title{font-size:15px;font-weight:700;margin-top:2px}
  .cover-date{position:absolute;left:4px;top:164px;width:130px;height:26px;background:var(--slate);clip-path:polygon(0 0,100% 0,86% 100%,0 100%);color:#fff;font-size:5.5px;padding:10px 0 0 30px}
  .cover-art{position:absolute;left:108px;top:262px;width:170px;height:98px;background:linear-gradient(135deg,rgba(215,25,32,0) 20%,rgba(215,25,32,.18) 100%)}

  /* toc */
  .toc{position:absolute;left:32px;right:32px;top:66px;font-size:4.6px}
  .toc li{list-style:none;display:flex;align-items:flex-end;margin-bottom:6.5px;color:#333}
  .toc li.main{font-weight:700;text-transform:uppercase;margin-top:4px;color:var(--ink)}
  .toc li .lead{flex:1;border-bottom:.6px dotted #555;margin:0 2px 1px}
  .toc li .two{line-height:1.3}

  /* tables */
  table{border-collapse:collapse;width:100%;font-size:4.5px;text-align:center;margin:8px 0}
  .scope-table th{height:22px;color:#fff;font-family:var(--head);font-weight:600;font-size:5.5px}
  .scope-table th.blank{background:var(--slate)}
  .scope-table th.r{background:var(--red)}
  .scope-table th.g{background:var(--grey)}
  .scope-table td{height:16px;background:var(--slate-2);color:#fff;border-top:1px solid #3e434a}
  .scope-table td:first-child{text-align:left;padding-left:10px}
  .obs-table th{height:22px;color:#fff;font-family:var(--head);font-weight:600;font-size:5px}
  .obs-table th.g{background:#8c8f93}
  .obs-table th.d{background:var(--slate)}
  .obs-table td{height:16px;background:#f3f3f3;color:#333}
  .obs-table tr:nth-child(even) td{background:#e9e9e9}
  .obs-table td:first-child{text-align:left;padding-left:4px}

  /* severity */
  .severity{position:relative;width:252px;height:213px;margin-left:-14px;margin-top:6px}
  .severity svg{position:absolute;left:0;top:0}
  .sev-label{position:absolute;top:85px;width:63px;height:24px;display:flex;align-items:center;justify-content:center;color:#fff;font-family:var(--head);font-weight:700;font-size:7px}
  .sev-text{position:absolute;top:113px;width:55px;font-size:4.3px;line-height:1.4;text-align:justify;color:#333}

  /* summary table */
  .find-table{margin-top:12px}
  .find-table .cap{background:var(--red);color:#fff;height:32px;font-family:var(--head);font-weight:700;font-size:7px;display:flex;align-items:center;padding-left:15px}
  .find-table table{margin:0}
  .find-table th{background:var(--slate);color:#fff;height:22px;font-size:5px;font-weight:600}
  .find-table th:first-child{text-align:left;padding-left:13px}
  .find-table td{background:#eeeeee;height:23px;font-size:4.5px}
  .find-table td:first-child{text-align:left;padding-left:13px;border-right:1px solid #fff}
  .c-crit{color:#555}.c-high{color:var(--high)}.c-med{color:var(--med)}.c-low{color:var(--low)}

  /* detailed observations */
  .detail .content{top:44px}
  .level{position:absolute;right:12px;top:63px;display:flex;align-items:center;gap:4px;font-family:var(--head);font-weight:600;font-size:10.5px;color:var(--accent)}
  .level span{border-bottom:1px solid var(--accent);padding:0 0 1px 2px}
  .level-dot{width:19px;height:19px;border-radius:50%;background:var(--accent);display:flex;align-items:center;justify-content:center}
  .spine-back{position:absolute;left:20px;top:100px;width:20px;height:172px;background:#dedede;clip-path:polygon(0 6%,100% 0,100% 100%,0 94%)}
  .spine{position:absolute;left:14px;top:110px;width:12px;height:146px;background:#6d6e71;border-radius:2px}
  .spine span{position:absolute;left:50%;top:50%;transform:translate(-50%,-50%) rotate(-90deg);white-space:nowrap;color:#fff;font-family:var(--head);font-weight:600;font-size:5px}
  .hex{position:absolute;left:34px;width:24px;height:24px;background:#111;clip-path:polygon(25% 0,75% 0,100% 50%,75% 100%,25% 100%,0 50%);display:flex;align-items:center;justify-content:center}
  .step{position:absolute;left:52px;width:122px;height:11px;background:var(--accent);clip-path:polygon(0 0,94% 0,100% 50%,94% 100%,0 100%);color:#fff;font-family:var(--head);font-weight:600;font-size:5px;display:flex;align-items:center;padding-left:14px}
  .block{position:absolute;left:58px;right:12px}
  .block ul{padding-left:10px;font-size:4.4px;line-height:1.4;color:#333;margin-top:2px}
  .shot{position:absolute;left:63px;top:140px;width:94px;height:64px;background:linear-gradient(180deg,#e9edf3,#cfd6e0);border:1px solid #bbb}
  .caption{position:absolute;left:164px;top:146px;font-size:4.5px;line-height:1.9;color:#333}
  .assets{position:absolute;left:62px;top:294px;font-size:4.4px;line-height:1.45;padding-left:8px}

  /* contact */
  .photo{position:absolute;left:32px;top:74px;width:220px;height:147px;background:linear-gradient(160deg,#e6e6e6,#a9a9a9)}
  .contact-list{position:absolute;left:32px;top:236px;list-style:none}
  .contact-list li{display:flex;gap:5px;margin-bottom:6px}
  .contact-list .ico{width:9px;height:9px;border-radius:50%;background:var(--red);display:flex;align-items:center;justify-content:center}
  .contact-list b{display:block;color:var(--red);font-size:5.5px;font-weight:600}
  .contact-list small{display:block;font-size:4.3px;color:#333}
</style>
</head>
<body>

<div class="sheet-row row-1">
  <!-- cover -->
  <section class="page cover">
    <div class="brand"><i></i>PROBEWISE</div>
    <div class="cover-title"><div class="client">Client Name</div><div class="title">Engagement Title</div></div>
    <div class="cover-date">Month Day, Year</div>
    <div class="cover-art" role="img" aria-label="Red low-poly wireframe network graphic"></div>
  </section>

  <!-- contents -->
  <section class="page">
    <div class="brand"><i></i>PROBEWISE</div>
    <ul class="toc">
      <li class="main">Engagement Overview<span class="lead"></span>2</li>
      <li>Engagement Scope<span class="lead"></span>2</li>
      <li>Engagement Summary<span class="lead"></span>3</li>
      <li>Key Observations<span class="lead"></span>3</li>
      <li class="main">Technical Overview<span class="lead"></span>4</li>
      <li>Severity Ratings<span class="lead"></span>4</li>
      <li>Summary Of Findings<span class="lead"></span>5</li>
      <li><span class="two">Detailed Observations<br>&nbsp;Critical Findings</span><span class="lead"></span>6</li>
      <li><span class="two">Detailed Observations<br>&nbsp;High Findings</span><span class="lead"></span>7</li>
      <li><span class="two">Detailed Observations<br>&nbsp;Medium Findings</span><span class="lead"></span>8</li>
      <li><span class="two">Detailed Observations<br>&nbsp;Low Findings</span><span class="lead"></span>9</li>
      <li class="main">Appendix 01<span class="lead"></span>10</li>
      <li>Engagement Methodology<span class="lead"></span>10</li>
      <li class="main">Our Contact<span class="lead"></span>11</li>
    </ul>
    <footer class="page-foot"><div class="band">Client Name <span>Engagement Title</span><span class="num">1</span></div><div class="tab"></div></footer>
  </section>

  <!-- scope -->
  <section class="page">
    <div class="brand"><i></i>PROBEWISE</div>
    <div class="content" style="top:56px">
      <p class="txt">This report summarises the security assessment performed for the client during the agreed testing window. It explains the goals of the work, the systems that were in scope, the methods our team followed and the main results that the client should review with care.</p>
      <div class="gap"></div>
      <h2>Engagement Scope</h2>
      <p class="txt">The scope covered external hosts, internal servers and the web portal listed below. Testing was limited to the agreed address ranges and took place outside business hours.</p>
      <table class="scope-table">
        <tr><th class="blank"></th><th class="r">Column 1</th><th class="g">Column 2</th><th class="r">Column 3</th></tr>
        <tr><td>Description 1</td><td>1</td><td>2</td><td>3</td></tr>
        <tr><td>Description 2</td><td>Text 1</td><td>Text 2</td><td>Text 3</td></tr>
        <tr><td>Description 3</td><td>• Bullet 1a</td><td>• Bullet 2a</td><td>• Bullet 3a</td></tr>
        <tr><td>Description 4</td><td>• Bullet 1b</td><td>• Bullet 2b</td><td>• Bullet 3b</td></tr>
      </table>
      <p class="txt">Each finding was verified by hand before it was added to this report. Results reflect the state of the systems at the time of testing and may change after updates.</p>
    </div>
    <footer class="page-foot"><div class="band">Client Name <span>Engagement Title</span><span class="num">2</span></div><div class="tab"></div></footer>
  </section>

  <!-- summary -->
  <section class="page">
    <div class="brand"><i></i>PROBEWISE</div>
    <div class="content" style="top:44px">
      <h2>Engagement Summary</h2>
      <p class="txt">This report summarises the security assessment performed for the client during the agreed testing window. It explains the goals of the work, the systems that were in scope, the methods our team followed and the main results that the client should review with care.</p>
      <div class="gap"></div>
      <h2>Key Observations</h2>
      <p class="txt">The scope covered external hosts, internal servers and the web portal listed below. Testing was limited to the agreed address ranges and took place outside business hours.</p>
      <table class="obs-table">
        <tr><th class="g"></th><th class="d">Column 1</th><th class="g">Column 2</th><th class="d">Column 3</th><th class="g">Column 4</th></tr>
        <tr><td>Description 1</td><td>Text</td><td>Text</td><td>Text</td><td>Text</td></tr>
        <tr><td>Description 2</td><td>Number 1</td><td>Number 2</td><td>Number 3</td><td>Number 4</td></tr>
        <tr><td>Description 3</td><td>Text</td><td>Text</td><td>Text</td><td>Text</td></tr>
        <tr><td>Description 4</td><td>Number 1</td><td>Number 2</td><td>Number 3</td><td>Number 4</td></tr>
      </table>
    </div>
    <footer class="page-foot"><div class="band">Client Name <span>Engagement Title</span><span class="num">3</span></div><div class="tab"></div></footer>
  </section>
</div>

<div class="sheet-row row-2">
  <!-- technical overview -->
  <section class="page">
    <div class="brand"><i></i>PROBEWISE</div>
    <div class="content" style="top:46px">
      <h2 class="red">Technical Overview</h2>
      <p class="txt">This report summarises the security assessment performed for the client during the agreed testing window. It explains the goals of the work, the systems that were in scope, the methods our team followed and the main results that the client should review with care.</p>
      <div class="gap" style="height:6px"></div>
      <h3>Severity Ratings</h3>
      <div class="severity">
        <svg width="252" height="213" viewBox="0 0 252 213">
          <g>
            <rect x="0" y="109" width="62" height="104" fill="#c8eef8"/>
            <polygon points="0,85 0,80 11,78 51,78 62,80 62,85" fill="#1687a8"/>
            <polygon points="11,85 11,58 31,48 51,58 51,85" fill="var(--low)"/>
            <rect x="0" y="85" width="62" height="24" fill="var(--low)"/>
            <circle cx="31" cy="68" r="9" fill="#fff"/>
            <rect x="27" y="68" width="2" height="4" fill="var(--low)"/><rect x="30" y="65" width="2" height="7" fill="var(--low)"/><rect x="33" y="62" width="2" height="10" fill="var(--low)"/>
          </g>
          <g>
            <rect x="63" y="109" width="62" height="104" fill="#fde0cc"/>
            <polygon points="63,85 63,80 74,78 114,78 125,80 125,85" fill="#c95609"/>
            <polygon points="74,85 74,42 94,32 114,42 114,85" fill="var(--med)"/>
            <rect x="63" y="85" width="62" height="24" fill="var(--med)"/>
            <circle cx="94" cy="53" r="9" fill="#fff"/>
            <rect x="90" y="53" width="2" height="4" fill="var(--med)"/><rect x="93" y="50" width="2" height="7" fill="var(--med)"/><rect x="96" y="47" width="2" height="10" fill="var(--med)"/>
          </g>
          <g>
            <rect x="126" y="109" width="62" height="104" fill="#f8d0d0"/>
            <polygon points="126,85 126,80 137,78 177,78 188,80 188,85" fill="#a91217"/>
            <polygon points="137,85 137,27 157,17 177,27 177,85" fill="var(--high)"/>
            <rect x="126" y="85" width="62" height="24" fill="var(--high)"/>
            <circle cx="157" cy="38" r="9" fill="#fff"/>
            <rect x="153" y="38" width="2" height="4" fill="var(--high)"/><rect x="156" y="35" width="2" height="7" fill="var(--high)"/><rect x="159" y="32" width="2" height="10" fill="var(--high)"/>
          </g>
          <g>
            <rect x="189" y="109" width="63" height="104" fill="#e0dbd5"/>
            <polygon points="189,85 189,80 200,78 240,78 252,80 252,85" fill="#352d26"/>
            <polygon points="200,85 200,14 220,4 240,14 240,85" fill="var(--crit)"/>
            <rect x="189" y="85" width="63" height="24" fill="var(--crit)"/>
            <circle cx="220" cy="25" r="9" fill="#fff"/>
            <rect x="216" y="25" width="2" height="4" fill="var(--crit)"/><rect x="219" y="22" width="2" height="7" fill="var(--crit)"/><rect x="222" y="19" width="2" height="10" fill="var(--crit)"/>
          </g>
        </svg>
        <div class="sev-label" style="left:0">LOW</div>
        <div class="sev-label" style="left:63px">MEDIUM</div>
        <div class="sev-label" style="left:126px">HIGH</div>
        <div class="sev-label" style="left:189px">CRITICAL</div>
        <p class="sev-text" style="left:4px">Issues at this level carry limited risk on their own. They should be fixed during normal upkeep and tracked until the change is confirmed.</p>
        <p class="sev-text" style="left:67px">Issues at this level carry moderate risk and may aid an attacker. They should be fixed within the next planned cycle and retested once done.</p>
        <p class="sev-text" style="left:130px">Issues at this level carry serious risk to data and systems. They should be fixed promptly, ideally within days, and checked again by the team.</p>
        <p class="sev-text" style="left:193px">Issues at this level allow direct compromise of key systems. They need urgent action, a temporary control if required, and immediate retesting.</p>
      </div>
    </div>
    <footer class="page-foot"><div class="band">Client Name <span>Engagement Title</span><span class="num">4</span></div><div class="tab"></div></footer>
  </section>

  <!-- summary of findings -->
  <section class="page">
    <div class="brand"><i></i>PROBEWISE</div>
    <div class="content" style="top:46px">
      <h2>Summary Of Findings</h2>
      <p class="txt">The scope covered external hosts, internal servers and the web portal listed below. Testing was limited to the agreed address ranges and took place outside business hours.</p>
      <div class="find-table">
        <div class="cap">Table 3</div>
        <table>
          <tr><th>Finding Name</th><th>Severity</th></tr>
          <tr><td class="c-crit">Critical Finding Title</td><td class="c-crit">Critical</td></tr>
          <tr><td class="c-high">High Finding Title</td><td class="c-high">High</td></tr>
          <tr><td class="c-med">Medium Finding Title</td><td class="c-med">Medium</td></tr>
          <tr><td class="c-low">Low Finding Title</td><td class="c-low">Low</td></tr>
        </table>
      </div>
    </div>
    <footer class="page-foot"><div class="band">Client Name <span>Engagement Title</span><span class="num">5</span></div><div class="tab"></div></footer>
  </section>

  <!-- critical -->
  <section class="page detail" style="--accent:var(--crit)">
    <div class="brand"><i></i>PROBEWISE</div>
    <div class="content"><h2>Detailed Observations</h2></div>
    <div class="level"><span>Critical Findings</span><div class="level-dot"><svg width="10" height="9"><rect x="0" y="5" width="2" height="4" fill="#fff"/><rect x="4" y="3" width="2" height="6" fill="#fff"/><rect x="8" y="0" width="2" height="9" fill="#fff"/></svg></div></div>
    <div class="spine-back"></div><div class="spine"><span>Insecure Configurations Identified</span></div>
    <div class="hex" style="top:77px"><svg width="10" height="10"><circle cx="4" cy="4" r="3" fill="none" stroke="#fff" stroke-width="1.3"/><line x1="6.2" y1="6.2" x2="9.5" y2="9.5" stroke="#fff" stroke-width="1.5"/></svg></div>
    <div class="step" style="top:83px">Observation</div>
    <div class="block" style="top:97px"><p class="txt">A misconfigured service was found on the host below. It exposes details that could help an attacker plan further steps against the network.</p></div>
    <div class="hex" style="top:118px"><svg width="10" height="10"><rect x="1.5" y="1.5" width="7" height="8" fill="none" stroke="#fff" stroke-width="1.1"/><rect x="3.5" y="0.5" width="3" height="2" fill="#fff"/></svg></div>
    <div class="step" style="top:124px">Recommendation</div>
    <div class="shot" role="img" aria-label="Screenshot of the tool output"></div>
    <div class="caption">Figure #1 -<br>This is the Caption<br>for the screenshot</div>
    <div class="hex" style="top:210px"><svg width="10" height="10"><rect x="0.5" y="3" width="9" height="6" fill="none" stroke="#fff" stroke-width="1.1"/><rect x="3.5" y="1" width="3" height="2" fill="none" stroke="#fff" stroke-width="1"/></svg></div>
    <div class="step" style="top:216px">Evidence</div>
    <div class="block" style="top:230px"><p class="txt">The request and response shown above confirm the issue on each listed asset.</p>
      <ul><li>Service banner revealed the exact software version in use.</li><li>Default settings remained active after the last update was applied.</li></ul></div>
    <div class="hex" style="top:273px"><svg width="10" height="10"><circle cx="4" cy="4" r="3" fill="none" stroke="#fff" stroke-width="1.3"/><line x1="6.2" y1="6.2" x2="9.5" y2="9.5" stroke="#fff" stroke-width="1.5"/></svg></div>
    <div class="step" style="top:279px">Assets Affected</div>
    <ul class="assets"><li>127.0.0.1</li><li>127.0.0.2</li><li>127.0.0.3</li></ul>
    <footer class="page-foot"><div class="band">Client Name <span>Engagement Title</span><span class="num">6</span></div><div class="tab"></div></footer>
  </section>

  <!-- high -->
  <section class="page detail" style="--accent:var(--high)">
    <div class="brand"><i></i>PROBEWISE</div>
    <div class="content"><h2>Detailed Observations</h2></div>
    <div class="level"><span>High Findings</span><div class="level-dot"><svg width="10" height="9"><rect x="0" y="5" width="2" height="4" fill="#fff"/><rect x="4" y="3" width="2" height="6" fill="#fff"/><rect x="8" y="0" width="2" height="9" fill="#fff"/></svg></div></div>
    <div class="spine-back"></div><div class="spine"><span>Insecure Configurations Identified</span></div>
    <div class="hex" style="top:77px"><svg width="10" height="10"><circle cx="4" cy="4" r="3" fill="none" stroke="#fff" stroke-width="1.3"/><line x1="6.2" y1="6.2" x2="9.5" y2="9.5" stroke="#fff" stroke-width="1.5"/></svg></div>
    <div class="step" style="top:83px">Observation</div>
    <div class="block" style="top:97px"><p class="txt">A misconfigured service was found on the host below. It exposes details that could help an attacker plan further steps against the network.</p></div>
    <div class="hex" style="top:118px"><svg width="10" height="10"><rect x="1.5" y="1.5" width="7" height="8" fill="none" stroke="#fff" stroke-width="1.1"/><rect x="3.5" y="0.5" width="3" height="2" fill="#fff"/></svg></div>
    <div class="step" style="top:124px">Recommendation</div>
    <div class="shot" role="img" aria-label="Screenshot of the tool output"></div>
    <div class="caption">Figure #1 -<br>This is the Caption<br>for the screenshot</div>
    <div class="hex" style="top:210px"><svg width="10" height="10"><rect x="0.5" y="3" width="9" height="6" fill="none" stroke="#fff" stroke-width="1.1"/><rect x="3.5" y="1" width="3" height="2" fill="none" stroke="#fff" stroke-width="1"/></svg></div>
    <div class="step" style="top:216px">Evidence</div>
    <div class="block" style="top:230px"><p class="txt">The request and response shown above confirm the issue on each listed asset.</p>
      <ul><li>Service banner revealed the exact software version in use.</li><li>Default settings remained active after the last update was applied.</li></ul></div>
    <div class="hex" style="top:273px"><svg width="10" height="10"><circle cx="4" cy="4" r="3" fill="none" stroke="#fff" stroke-width="1.3"/><line x1="6.2" y1="6.2" x2="9.5" y2="9.5" stroke="#fff" stroke-width="1.5"/></svg></div>
    <div class="step" style="top:279px">Assets Affected</div>
    <ul class="assets"><li>127.0.0.1</li><li>127.0.0.2</li><li>127.0.0.3</li></ul>
    <footer class="page-foot"><div class="band">Client Name <span>Engagement Title</span><span class="num">7</span></div><div class="tab"></div></footer>
  </section>
</div>

<div class="sheet-row row-3">
  <!-- medium -->
  <section class="page detail" style="--accent:var(--med)">
    <div class="brand"><i></i>PROBEWISE</div>
    <div class="content"><h2>Detailed Observations</h2></div>
    <div class="level"><span>Medium Findings</span><div class="level-dot"><svg width="10" height="9"><rect x="0" y="5" width="2" height="4" fill="#fff"/><rect x="4" y="3" width="2" height="6" fill="#fff"/><rect x="8" y="0" width="2" height="9" fill="#fff"/></svg></div></div>
    <div class="spine-back"></div><div class="spine"><span>Insecure Configurations Identified</span></div>
    <div class="hex" style="top:77px"><svg width="10" height="10"><circle cx="4" cy="4" r="3" fill="none" stroke="#fff" stroke-width="1.3"/><line x1="6.2" y1="6.2" x2="9.5" y2="9.5" stroke="#fff" stroke-width="1.5"/></svg></div>
    <div class="step" style="top:83px">Observation</div>
    <div class="block" style="top:97px"><p class="txt">A misconfigured service was found on the host below. It exposes details that could help an attacker plan further steps against the network.</p></div>
    <div class="hex" style="top:118px"><svg width="10" height="10"><rect x="1.5" y="1.5" width="7" height="8" fill="none" stroke="#fff" stroke-width="1.1"/><rect x="3.5" y="0.5" width="3" height="2" fill="#fff"/></svg></div>
    <div class="step" style="top:124px">Recommendation</div>
    <div class="shot" role="img" aria-label="Screenshot of the tool output"></div>
    <div class="caption">Figure #1 -<br>This is the Caption<br>for the screenshot</div>
    <div class="hex" style="top:210px"><svg width="10" height="10"><rect x="0.5" y="3" width="9" height="6" fill="none" stroke="#fff" stroke-width="1.1"/><rect x="3.5" y="1" width="3" height="2" fill="none" stroke="#fff" stroke-width="1"/></svg></div>
    <div class="step" style="top:216px">Evidence</div>
    <div class="block" style="top:230px"><p class="txt">The request and response shown above confirm the issue on each listed asset.</p>
      <ul><li>Service banner revealed the exact software version in use.</li><li>Default settings remained active after the last update was applied.</li></ul></div>
    <div class="hex" style="top:273px"><svg width="10" height="10"><circle cx="4" cy="4" r="3" fill="none" stroke="#fff" stroke-width="1.3"/><line x1="6.2" y1="6.2" x2="9.5" y2="9.5" stroke="#fff" stroke-width="1.5"/></svg></div>
    <div class="step" style="top:279px">Assets Affected</div>
    <ul class="assets"><li>127.0.0.1</li><li>127.0.0.2</li><li>127.0.0.3</li></ul>
    <footer class="page-foot"><div class="band">Client Name <span>Engagement Title</span><span class="num">8</span></div><div class="tab"></div></footer>
  </section>

  <!-- low -->
  <section class="page detail" style="--accent:var(--low)">
    <div class="brand"><i></i>PROBEWISE</div>
    <div class="content"><h2>Detailed Observations</h2></div>
    <div class="level"><span>Low Findings</span><div class="level-dot"><svg width="10" height="9"><rect x="0" y="5" width="2" height="4" fill="#fff"/><rect x="4" y="3" width="2" height="6" fill="#fff"/><rect x="8" y="0" width="2" height="9" fill="#fff"/></svg></div></div>
    <div class="spine-back"></div><div class="spine"><span>Insecure Configurations Identified</span></div>
    <div class="hex" style="top:77px"><svg width="10" height="10"><circle cx="4" cy="4" r="3" fill="none" stroke="#fff" stroke-width="1.3"/><line x1="6.2" y1="6.2" x2="9.5" y2="9.5" stroke="#fff" stroke-width="1.5"/></svg></div>
    <div class="step" style="top:83px">Observation</div>
    <div class="block" style="top:97px"><p class="txt">A misconfigured service was found on the host below. It exposes details that could help an attacker plan further steps against the network.</p></div>
    <div class="hex" style="top:118px"><svg width="10" height="10"><rect x="1.5" y="1.5" width="7" height="8" fill="none" stroke="#fff" stroke-width="1.1"/><rect x="3.5" y="0.5" width="3" height="2" fill="#fff"/></svg></div>
    <div class="step" style="top:124px">Recommendation</div>
    <div class="shot" role="img" aria-label="Screenshot of the tool output"></div>
    <div class="caption">Figure #1 -<br>This is the Caption<br>for the screenshot</div>
    <div class="hex" style="top:210px"><svg width="10" height="10"><rect x="0.5" y="3" width="9" height="6" fill="none" stroke="#fff" stroke-width="1.1"/><rect x="3.5" y="1" width="3" height="2" fill="none" stroke="#fff" stroke-width="1"/></svg></div>
    <div class="step" style="top:216px">Evidence</div>
    <div class="block" style="top:230px"><p class="txt">The request and response shown above confirm the issue on each listed asset.</p>
      <ul><li>Service banner revealed the exact software version in use.</li><li>Default settings remained active after the last update was applied.</li></ul></div>
    <div class="hex" style="top:273px"><svg width="10" height="10"><circle cx="4" cy="4" r="3" fill="none" stroke="#fff" stroke-width="1.3"/><line x1="6.2" y1="6.2" x2="9.5" y2="9.5" stroke="#fff" stroke-width="1.5"/></svg></div>
    <div class="step" style="top:279px">Assets Affected</div>
    <ul class="assets"><li>127.0.0.1</li><li>127.0.0.2</li><li>127.0.0.3</li></ul>
    <footer class="page-foot"><div class="band">Client Name <span>Engagement Title</span><span class="num">9</span></div><div class="tab"></div></footer>
  </section>

  <!-- appendix -->
  <section class="page">
    <div class="brand"><i></i>PROBEWISE</div>
    <div class="content" style="top:46px">
      <h2 class="red" style="margin-bottom:1px">Appendix 01</h2>
      <h2>Engagement Methodology</h2>
      <p class="txt">This report summarises the security assessment performed for the client during the agreed testing window. It explains the goals of the work, the systems that were in scope, the methods our team followed and the main results that the client should review with care.</p>
    </div>
    <footer class="page-foot"><div class="band">Client Name <span>Engagement Title</span><span class="num">10</span></div><div class="tab"></div></footer>
  </section>

  <!-- contact -->
  <section class="page">
    <div class="brand"><i></i>PROBEWISE</div>
    <div class="content" style="top:46px"><h2 class="red">Our Contact</h2></div>
    <div class="photo" role="img" aria-label="Grey-toned photo of a laptop on a desk with coffee mugs"></div>
    <ul class="contact-list">
      <li><span class="ico"><svg width="5" height="6"><path d="M2.5 0.5a2 2 0 0 1 2 2c0 1.5-2 3.3-2 3.3S0.5 4 0.5 2.5a2 2 0 0 1 2-2z" fill="#fff"/></svg></span><div><b>Address</b><small>567 Street Name, City, 12345</small></div></li>
      <li><span class="ico"><svg width="5" height="5"><path d="M1 0.5l1 1.2-0.6 0.8a3 3 0 0 0 1.2 1.2l0.8-0.6 1.2 1-0.6 0.8C2.5 4.8 0.2 2.5 0.3 1z" fill="#fff"/></svg></span><div><b>Phone</b><small>123-456-789 01</small></div></li>
      <li><span class="ico"><svg width="6" height="5"><rect x="0.5" y="0.8" width="5" height="3.4" fill="none" stroke="#fff" stroke-width=".7"/><path d="M0.5 0.8l2.5 2 2.5-2" fill="none" stroke="#fff" stroke-width=".7"/></svg></span><div><b>Email</b><small>contact@probewise.com</small></div></li>
      <li><span class="ico"><svg width="6" height="6"><circle cx="3" cy="3" r="2.4" fill="none" stroke="#fff" stroke-width=".7"/><line x1="0.6" y1="3" x2="5.4" y2="3" stroke="#fff" stroke-width=".6"/><ellipse cx="3" cy="3" rx="1" ry="2.4" fill="none" stroke="#fff" stroke-width=".6"/></svg></span><div><b>Website</b><small>www.probewise.com</small></div></li>
    </ul>
    <footer class="page-foot"><div class="band">Client Name <span>Engagement Title</span><span class="num">11</span></div><div class="tab"></div></footer>
  </section>
</div>

</body>
</html>
```